menu buttom design

We are looking for a menu button design, similar too the one we have posted in the files section.
They must be quite big and prominent on the page. They will be down the right hand side of the website which has a large video player on as well. We would like them to look a little like TV buttons, not not cliched.
The titles on each button are as follows:
Whats new, Buy and sell, Join in, More TV, More Info, more web
The web page will be black.
PLEASE concentrate more on the colours and text that making the buttons different shapes.
It must look classy, sophistocated, beautiful design

Target Market(s)

Web Tv watchers

Requirements
Must have
• Should be similar to what I have uploaded on the file.
Should be rectangular, raised up to give button effect with some shine.
What we would really like to to have some sorts of graphics behind the text to show the various
pages. We would like more subtle, maybe pastel colours that work well together and a really nice font that works well.
Concentrate more on the colours and fonts and the overall look rather than different shapes.
These buttons are for mock up web pages, but when the pages are made we will us the buttons as templates and will animate them when you roll over them.

```html
<!DOCTYPE html>
<html lang="en">
<head>
<meta charset="utf-8">
<title>Menu Buttons</title>
<link href="https://fonts.googleapis.com/css2?family=Archivo+Black&family=Arimo:wght@700&display=swap" rel="stylesheet">
<style>
  :root {
    --page: #ffffff;
    --frame-light: #f4f4f4;
    --frame-mid: #c9c9c9;
    --frame-dark: #7d7d7d;
    --ink: #0a0a0a;
    --purple-top: #ece2f7; --purple: #b79bd9; --purple-edge: #3b49b8;
    --blue-top: #e2f5fd; --blue: #5fc3ef; --blue-edge: #1d5fc0;
    --green-top: #d9f3e1; --green: #41b86a; --green-edge: #137a3a;
    --orange-top: #fff3d6; --orange: #fbbf4f; --orange-edge: #8a4a12;
    --red-top: #fde2d8; --red: #f07a5a; --red-edge: #7c1a12;
    --yellow-top: #fffbd9; --yellow: #f5e574; --yellow-edge: #3a2a10;
  }
  html, body { margin: 0; padding: 0; }
  body {
    width: 1200px; height: 3268px; overflow: hidden;
    background: var(--page); position: relative;
    font-family: "Archivo Black", "Arial Black", sans-serif;
  }
  .menu-button {
    position: absolute; left: 128px; width: 912px; height: 420px;
    box-sizing: border-box; border-radius: 84px;
    background: linear-gradient(180deg, var(--frame-light) 0%, var(--frame-mid) 55%, #a9a9a9 100%);
    border: 8px solid var(--frame-dark);
    box-shadow: inset 0 6px 8px rgba(255,255,255,.9), inset 0 -10px 14px rgba(0,0,0,.18);
  }
  .menu-button__face {
    position: absolute; left: 48px; right: 48px; top: 40px; bottom: 40px;
    border-radius: 52px; overflow: hidden;
    border: 10px solid var(--edge);
    background: linear-gradient(180deg, var(--top) 0%, var(--base) 60%, var(--base) 100%);
    box-shadow: 0 6px 0 rgba(0,0,0,.25), inset 0 -12px 18px rgba(0,0,0,.12);
  }
  .menu-button__face::before {
    content: ""; position: absolute; left: 24px; right: 24px; top: 8px; height: 44%;
    border-radius: 40px 40px 60px 60px;
    background: linear-gradient(180deg, rgba(255,255,255,.85), rgba(255,255,255,.15));
  }
  .menu-button__icon {
    position: absolute; left: 40px; top: 50%; transform: translateY(-50%);
    width: 240px; height: 200px; border-radius: 20px;
    background: var(--icon);
  }
  .menu-button__label {
    position: absolute; right: 40px; top: 50%; transform: translateY(-50%);
    width: 470px; text-align: center;
    font-size: 112px; line-height: 104px; color: var(--ink);
    text-shadow: 4px 6px 0 rgba(0,0,0,.35), 0 0 10px rgba(255,255,255,.9);
  }
  .is-whats-new { top: 60px; --top: var(--purple-top); --base: var(--purple); --edge: var(--purple-edge); --icon: linear-gradient(160deg,#ffb7de,#f05aa8); }
  .is-buy-sell { top: 660px; --top: var(--blue-top); --base: var(--blue); --edge: var(--blue-edge); --icon: linear-gradient(180deg,#f7e3a3,#d6a94a); }
  .is-join-in { top: 1200px; --top: var(--green-top); --base: var(--green); --edge: var(--green-edge); --icon: linear-gradient(180deg,#f3b4c9,#7ec6ee); }
  .is-more-tv { top: 1740px; --top: var(--orange-top); --base: var(--orange); --edge: var(--orange-edge); --icon: linear-gradient(160deg,#5d84d8,#1b2f7c); }
  .is-more-web { top: 2288px; --top: var(--red-top); --base: var(--red); --edge: var(--red-edge); --icon: linear-gradient(160deg,#e8f0fb,#3b7ad6); }
  .is-join-in .menu-button__label { width: 520px; right: 24px; }
  .is-login { top: 2820px; --top: var(--yellow-top); --base: var(--yellow); --edge: var(--yellow-edge); }
  .login__title {
    position: absolute; left: 10px; top: 50%; width: 260px;
    transform: translate(-90px,-50%) rotate(-90deg); text-align: center;
    font-size: 84px; color: var(--ink);
    text-shadow: 3px 4px 0 rgba(0,0,0,.3);
  }
  .login__field {
    position: absolute; left: 172px; right: 40px; height: 104px;
    box-sizing: border-box; background: #fff;
    border: 6px solid #3a3a3a; border-radius: 6px;
    font-family: "Arimo", Arial, sans-serif; font-size: 46px; color: #d2d2d2;
    display: flex; align-items: center; justify-content: center;
    box-shadow: inset 0 4px 6px rgba(0,0,0,.15);
  }
  .login__field--password { top: 28px; }
  .login__field--screen { bottom: 28px; }
</style>
</head>
<body>
  <nav class="menu">
    <a class="menu-button is-whats-new"><div class="menu-button__face">
      <div class="menu-button__icon" role="img" aria-label="Stack of pink gift boxes"></div>
      <div class="menu-button__label">Whats<br>New</div></div></a>
    <a class="menu-button is-buy-sell"><div class="menu-button__face">
      <div class="menu-button__icon" role="img" aria-label="Wicker shopping basket"></div>
      <div class="menu-button__label">Buy &amp;<br>Sell</div></div></a>
    <a class="menu-button is-join-in"><div class="menu-button__face">
      <div class="menu-button__icon" role="img" aria-label="Two figures shaking hands"></div>
      <div class="menu-button__label">Join In</div></div></a>
    <a class="menu-button is-more-tv"><div class="menu-button__face">
      <div class="menu-button__icon" role="img" aria-label="Flat screen monitor"></div>
      <div class="menu-button__label">More<br>Tv</div></div></a>
    <a class="menu-button is-more-web"><div class="menu-button__face">
      <div class="menu-button__icon" role="img" aria-label="Web browser box"></div>
      <div class="menu-button__label">More<br>Web</div></div></a>
    <div class="menu-button is-login"><div class="menu-button__face">
      <div class="login__title">Login</div>
      <div class="login__field login__field--password">password</div>
      <div class="login__field login__field--screen">screen name</div></div></div>
  </nav>
</body>
</html>
```